依頼詳細
医薬分野のLPページはカッチリした、ビジネスや商材感のあるものよりは、フランクで親しみやすいものであると嬉しいです。
今回はコーディングなど一切必要ございません。
募集したいものとして、デザイン案やワイヤーフレーム(ラフ)など雰囲気のわかるもので結構です。
また、一度デザインしたものであれば事例でも構いません!
事例の場合は手書きのワイヤーフレーム(ラフ)をいただけると、文字やフォームをどの辺に置くかイメージが共有できるので嬉しいです。
サイトURL
ページ数
1ページ
希望イメージ
シンプル 複雑
単色 カラフル
暗い 明るい
日常 高級
遊び心 厳粛
未来的 伝統的
女性的 男性的
希望する色
黄・オレンジ系
納品ファイル
• 高解像度JPG (.jpg)
• PNG形式 (.png)
補足説明
※4/15 追記
画像素材を作りました。
■ 選んだ理由

訳文翻訳はどうしてもかたいイメージがあるのですが、とてもわかりやすかったです。
難しいことを簡単にしてくれるイメージが伝わるので決めました。

■ 提案者全員のお礼・コメント

難しい課題だったのにも関わらずご提案いただきありがとうございました!クライアントとも密に精査させていただきました。皆様に御礼申し上げます。

```html
<!DOCTYPE html>
<html lang="ja">
<head>
<meta charset="utf-8">
<title>訳文検証 無料トライアル</title>
<link rel="stylesheet" href="https://fonts.googleapis.com/css2?family=M+PLUS+1p:wght@500;700;800&display=swap">
<style>
  :root {
    --navy: #1f3247;
    --blue: #2a7cc7;
    --lime: #d8e35a;
    --paper: #f8fafc;
    --grid: #e1e9f1;
    --white: #ffffff;
    --figure-light: #f3f1e4;
    --figure-tone: #e0e6a0;
  }
  * { margin: 0; padding: 0; box-sizing: border-box; }
  html, body { width: 675px; height: 1200px; overflow: hidden; }
  body {
    font-family: "M PLUS 1p", sans-serif;
    color: var(--navy);
    background-color: var(--paper);
    background-image:
      linear-gradient(var(--grid) 2px, transparent 2px),
      linear-gradient(90deg, var(--grid) 2px, transparent 2px);
    background-size: 45px 45px;
    background-position: -10px -5px;
    position: relative;
  }
  .tagline {
    position: absolute;
    left: 0; right: 0; top: 72px;
    text-align: center;
  }
  .tagline span {
    display: inline-block;
    font-size: 29px;
    font-weight: 700;
    color: var(--blue);
    letter-spacing: 1px;
    padding: 2px 14px;
    white-space: nowrap;
    background: linear-gradient(transparent 50%, var(--lime) 50%);
  }
  .headline {
    position: absolute;
    left: 78px; top: 190px;
    font-size: 51px;
    font-weight: 800;
    line-height: 1.5;
    letter-spacing: 2px;
    white-space: nowrap;
  }
  .speech-tail {
    position: absolute;
    left: 78px; top: 340px;
  }
  .figure {
    position: absolute;
    left: 160px; top: 398px;
    width: 460px; height: 492px;
    border-radius: 28px;
    background: linear-gradient(160deg, var(--figure-tone) 0%, var(--figure-light) 55%, #d9dde2 100%);
  }
  .banner {
    position: absolute;
    left: 0; right: 0; top: 898px;
    height: 76px;
    background: var(--blue);
    color: var(--white);
    font-size: 42px;
    font-weight: 800;
    letter-spacing: 3px;
    text-align: center;
    line-height: 76px;
  }
  .banner::after {
    content: "";
    position: absolute;
    left: 50%; bottom: -16px;
    transform: translateX(-50%);
    border-left: 16px solid transparent;
    border-right: 16px solid transparent;
    border-top: 17px solid var(--blue);
  }
  .features {
    position: absolute;
    left: 75px; top: 1020px;
    list-style: none;
  }
  .features li {
    display: flex;
    align-items: center;
    gap: 22px;
    font-size: 44px;
    font-weight: 800;
    letter-spacing: 2px;
    height: 66px;
  }
  .check { flex: none; }
</style>
</head>
<body>
  <p class="tagline"><span>切れ味鋭く、ソフトコミュニケーション</span></p>

  <h1 class="headline">訳文検証、<br>つらくありませんか?</h1>

  <svg class="speech-tail" width="260" height="46" viewBox="0 0 260 46" aria-hidden="true">
    <path d="M4 8 Q50 26 100 26 L112 40 L120 25 Q190 22 254 4" fill="none" stroke="#1f3247" stroke-width="4" stroke-linecap="round" stroke-linejoin="round"/>
  </svg>

  <div class="figure" role="img" aria-label="ノートパソコンの前で指を立てて説明する白衣の女性のイラスト"></div>

  <div class="banner">無料トライアル実施中!</div>

  <ul class="features">
    <li>
      <svg class="check" width="40" height="40" viewBox="0 0 40 40" aria-hidden="true">
        <rect x="2" y="2" width="36" height="36" fill="#fff" stroke="#2a7cc7" stroke-width="4"/>
        <path d="M10 20 L17 27 L30 12" fill="none" stroke="#2a7cc7" stroke-width="5" stroke-linecap="square"/>
      </svg>
      翻訳者用の用語挿入
    </li>
    <li>
      <svg class="check" width="40" height="40" viewBox="0 0 40 40" aria-hidden="true">
        <rect x="2" y="2" width="36" height="36" fill="#fff" stroke="#2a7cc7" stroke-width="4"/>
        <path d="M10 20 L17 27 L30 12" fill="none" stroke="#2a7cc7" stroke-width="5" stroke-linecap="square"/>
      </svg>
      英文和訳・和文英訳
    </li>
  </ul>
</body>
</html>
```